KWT Contracting services . Building and maintenance services, optic fibre installation

Business cards and logo design.I need a logo that I can use on business cards ,workwear and on my vehicles. I would like the KWT to be the main or larger text and contracting services to be the smaller or less important text.I like monograms, modern designs and repeating patterns symbols. I am also a Gemini and my favourite number is 22 so if this can be any inspiration to help with the design. Am thinking of the using German flag colours as a his is my family’s heritage. And the other 2 main colours I wear is black and white.But any ideas are appreciated.I do not need a design that is trade specific but a design that could be used for any business.

Target Market(s)

General public

Contact Information for Business Card

KWT Contracting Services ( front of business card)

(Back of business card)
Milo Brackwood
0471539264
Maintenance services
Optic fibre and data installation

Logo Text

Logo can just be pattern or monogram or incorporate KWT . I like the gemini star sign and the number 22

Colors
ec1f27
000000
fbee3e
ffffff

Requirements
Must have
• Logo and KWT Contracting Services on the front of business card
Nice to have
• Possible use of German flag colours.
• Modern design.
• Design to be able to be used on black or white background as I want to put it on clothing

```html
<!DOCTYPE html>
<html lang="en">
<head>
<meta charset="utf-8">
<title>KWT Contracting Services – Business Cards</title>
<link href="https://fonts.googleapis.com/css2?family=Montserrat:wght@400;500;700;800&display=swap" rel="stylesheet">
<style>
  :root {
    --brand-red: #7f1519;
    --paper: #ffffff;
    --ink-grey: #5a5a5a;
    --font: "Montserrat", Arial, sans-serif;
  }
  html, body {
    margin: 0;
    padding: 0;
    width: 1200px;
    height: 1200px;
    overflow: hidden;
    background: var(--paper);
    font-family: var(--font);
  }
  .board {
    position: relative;
    width: 1200px;
    height: 1200px;
  }
  .board-split {
    position: absolute;
    inset: 0;
  }
  .card {
    position: absolute;
    left: 275px;
    width: 650px;
    height: 385px;
    box-shadow: 6px 8px 10px rgba(0, 0, 0, 0.35);
  }
  .card-front {
    top: 185px;
    background: var(--brand-red);
    color: var(--paper);
  }
  .card-back {
    top: 630px;
    background: var(--paper);
  }

  /* wordmark */
  .wordmark-name {
    font-weight: 800;
    line-height: 1;
    letter-spacing: 2px;
  }
  .wordmark-tag {
    font-weight: 500;
    letter-spacing: 2.2px;
    white-space: nowrap;
  }

  .front-mark {
    position: absolute;
    left: 0;
    right: 0;
    top: 140px;
    text-align: center;
  }
  .front-mark .wordmark-name { font-size: 96px; }
  .front-mark .wordmark-tag { font-size: 15px; margin-top: 4px; }
  .front-url {
    position: absolute;
    left: 0;
    right: 0;
    top: 345px;
    text-align: center;
    font-size: 9px;
    letter-spacing: 1.6px;
  }

  .back-mark {
    position: absolute;
    left: 52px;
    top: 52px;
    color: var(--brand-red);
  }
  .back-mark .wordmark-name { font-size: 92px; }
  .back-mark .wordmark-tag { font-size: 14px; color: var(--ink-grey); margin-top: 1px; }

  .name-tab {
    position: absolute;
    left: 0;
    top: 211px;
    width: 28px;
    height: 52px;
    background: var(--brand-red);
  }
  .holder {
    position: absolute;
    left: 52px;
    top: 217px;
  }
  .holder-name {
    font-size: 20px;
    color: var(--brand-red);
    font-weight: 500;
    letter-spacing: 0.5px;
    line-height: 1;
  }
  .holder-name strong { font-weight: 800; }
  .holder-role {
    font-size: 14px;
    color: var(--ink-grey);
    margin-top: 4px;
  }
  .name-rule {
    position: absolute;
    left: 287px;
    right: 0;
    top: 227px;
    height: 2px;
    background: var(--brand-red);
  }
  .contact {
    position: absolute;
    left: 52px;
    top: 298px;
    font-size: 14px;
    line-height: 16.5px;
    color: var(--ink-grey);
  }
  .contact-label { color: var(--brand-red); }
  .services {
    position: absolute;
    right: 35px;
    top: 314px;
    margin: 0;
    padding: 0;
    list-style: none;
    text-align: right;
    font-size: 14px;
    line-height: 18px;
    color: var(--ink-grey);
  }
  .services li::after {
    content: "";
    display: inline-block;
    width: 6px;
    height: 6px;
    margin-left: 8px;
    border-radius: 50%;
    background: var(--brand-red);
    vertical-align: 1px;
  }
  .board-sign {
    position: absolute;
    left: 0;
    right: 0;
    top: 1148px;
    text-align: center;
    color: var(--paper);
  }
  .board-sign .wordmark-name { font-size: 26px; }
  .board-sign .wordmark-tag { font-size: 4px; letter-spacing: 0.6px; }
</style>
</head>
<body>
<main class="board">
  <svg class="board-split" width="1200" height="1200" viewBox="0 0 1200 1200" aria-hidden="true">
    <polygon points="1200,0 1200,1200 0,1200" fill="#7f1519"/>
  </svg>

  <section class="card card-front">
    <div class="front-mark">
      <div class="wordmark-name">KWT</div>
      <div class="wordmark-tag">CONTRACTING SERVICES</div>
    </div>
    <div class="front-url">www.kwtcontractingservices.com</div>
  </section>

  <section class="card card-back">
    <div class="back-mark">
      <div class="wordmark-name">KWT</div>
      <div class="wordmark-tag">CONTRACTING SERVICES</div>
    </div>
    <div class="name-tab"></div>
    <div class="holder">
      <div class="holder-name"><strong>MILO</strong> BRACKWOOD</div>
      <div class="holder-role">General Manager</div>
    </div>
    <div class="name-rule"></div>
    <div class="contact">
      <div class="contact-label">info:</div>
      <div>0471539264</div>
      <div>milo.brackwood@kwtmail.net</div>
    </div>
    <ul class="services">
      <li>Maintenance services</li>
      <li>Optic fibre and data installation</li>
    </ul>
  </section>

  <div class="board-sign">
    <div class="wordmark-name">KWT</div>
    <div class="wordmark-tag">CONTRACTING SERVICES</div>
  </div>
</main>
</body>
</html>
```